BrightHaven Webpage for Integrative and Holistic Psychiatric Practice

We need a webpage designed for a medical practice that focuses on integrative and holistic psychiatry. We focus on providing care to mothers and families. The name of the company is Bright Haven, incorporated, A Professional Medical Corporation.

We'd like the color palette to be earthy/natural with the same look and feel as our logo that's attached. We're not set on anything, so feel free to have fun with the palette. We just want it to be warm and inviting in particular for Moms!

We'd like to have our logo in the top left with links below it either centered or to the right. We really like websites like http://www.maplerivercare.example/home.html and http://www.tarrowfieldclinicpartners.example/site/ to give you an idea of what we're looking for.

For links, we're looking for the following. Dummy text is fine, we're still getting content together:

* Home
* About Us - this page would have headings for Directions, Staff, Appointment Scheduling
* Services Provided - headings for 8 different services
* Patient Resources - headings for Patient Forms, Fees, Articles
* FAQ
* Contact Us

The webpage will be hosted as an Cloudvane 9 Public Website, so feel free to use whatever DeskLoom integration you would like, but it's not necessary.

Thank you!

```html
<!DOCTYPE html>
<html lang="en">
<head>
<meta charset="utf-8">
<title>BrightHaven</title>
<link rel="stylesheet" href="https://fonts.googleapis.com/css2?family=Lato:wght@400;700&family=Oxygen:wght@400;700&display=swap">
<style>
:root{
  --green:#2f6800;
  --green-dark:#255200;
  --brown:#6b3300;
  --brown-text:#6e3b06;
  --page:#f2f3f1;
  --band:#e0e4dc;
  --panel:#cfcfcf;
  --ink:#333;
  --muted:#555;
  --nav:#3d5563;
  --white:#fff;
}
*{box-sizing:border-box;margin:0;padding:0}
html,body{width:935px;height:1200px;overflow:hidden}
body{position:relative;background:var(--page);font-family:"Oxygen",Arial,sans-serif;color:var(--ink)}
.abs{position:absolute}
.topbar{left:0;top:0;width:935px;height:22px;background:var(--green)}
.topbar-phone{right:16px;top:2px;color:var(--white);font-size:14px;font-weight:700;display:flex;align-items:center;gap:6px}
.header{left:0;top:22px;width:935px;height:58px;background:#f4f5f3}
.logo{left:128px;top:0;width:105px;height:80px;background:var(--white);display:flex;flex-direction:column;align-items:center;justify-content:center;gap:6px}
.logo-mark{width:22px;height:22px;border-radius:50%;background:var(--green)}
.logo-name{font-family:"Lato",sans-serif;font-size:13px;color:var(--green);font-weight:700}
.nav{right:114px;top:45px;display:flex;gap:24px;font-size:11.5px;color:var(--nav);text-transform:uppercase}
.nav .active{color:var(--green)}
.hero{left:0;top:80px;width:935px;height:280px;background:linear-gradient(90deg,#f5f5f4,#ececea)}
.hero-photo{left:375px;top:80px;width:560px;height:280px;background:linear-gradient(100deg,#eee9e2 0%,#e9d2bf 35%,#f0ddd0 60%,#a57f63 100%)}
.form-panel{left:111px;top:119px;width:352px;height:212px;background:var(--panel)}
.form-tab{left:201px;top:107px;width:171px;height:38px;background:var(--green);color:var(--white);font-family:"Lato",sans-serif;font-size:16px;display:flex;align-items:center;justify-content:center}
.field{position:absolute;width:141px;height:22px;background:var(--white);border:1px solid #bbb;font-size:7.5px;color:#666;padding:6px 9px}
.select::after{content:"";position:absolute;right:8px;top:9px;border:3px solid transparent;border-top-color:#777}
.form-submit{left:111px;top:288px;width:352px;height:43px;background:var(--green);color:var(--white);font-family:"Lato",sans-serif;font-size:13px;display:flex;align-items:center;justify-content:center}
.steps{left:0;top:360px;width:935px;height:155px;background:var(--band)}
.step{position:absolute;width:130px;text-align:center;top:382px}
.step svg{display:block;margin:0 auto}
.step-label{font-family:"Lato",sans-serif;color:var(--brown-text);font-size:16px;line-height:16px;margin-top:15px}
.dots{position:absolute;top:403px}
.section-title{font-family:"Lato",sans-serif;color:var(--green);font-size:16px;font-weight:400}
.rule{height:1px;background:#bbb}
.rule::before{content:"";display:block;width:32px;height:2px;background:var(--green);margin-top:-1px}
.video{left:104px;top:586px;width:290px;height:169px;border:1px solid #999;background:linear-gradient(160deg,#f4f1ec,#e4cab4 60%,#d6b493)}
.video-bar{left:104px;top:726px;width:290px;height:29px;background:#1f2a33}
.body-text{left:416px;top:582px;width:406px;font-size:8.4px;line-height:20.2px;color:#444;letter-spacing:.25px}
.lower{left:0;top:776px;width:935px;height:192px;background:var(--band)}
.divider-v{left:464px;top:796px;width:1px;height:160px;background:#c6c9c2}
.why-item{left:105px;width:215px;font-size:9.5px;line-height:14px;color:#333;padding-left:16px}
.why-item::before{content:"";position:absolute;left:0;top:2px;border:6px solid transparent;border-left:8px solid var(--green);border-right:0}
.read-more{left:105px;top:938px;height:21px;display:flex;font-size:9.5px;color:var(--white)}
.read-more span{background:var(--green);padding:4px 8px}
.read-more b{background:#1f2a33;width:22px;font-weight:400;text-align:center;padding-top:3px}
.quote-box{left:523px;top:840px;width:300px;height:100px;border:1px solid #999;border-radius:4px;background:#f3f4f2;overflow:hidden}
.quote-text{padding:10px 16px;font-size:9.5px;line-height:17px;font-style:italic;color:#444}
.quote-name{position:absolute;left:0;bottom:0;width:100%;height:24px;background:var(--green);color:var(--white);font-size:10px;padding:6px 14px}
.avatar{left:757px;top:900px;width:56px;height:56px;border-radius:50%;border:3px solid var(--white);background:linear-gradient(180deg,#6b4a35,#c9a185 55%,#dfe6ea)}
.footer{left:0;top:968px;width:935px;height:187px;background:var(--green)}
.footer-col{position:absolute;top:992px;color:var(--white)}
.footer-col h3{font-family:"Lato",sans-serif;font-weight:700;font-size:12.5px;line-height:15px;color:var(--white)}
.footer-rule{height:1px;background:rgba(255,255,255,.45);margin-top:6px}
.quick-links{list-style:none;font-size:10px;line-height:20px;margin-top:4px}
.quick-links li::before{content:"• "}
.contact-row{display:flex;gap:12px;font-size:9.5px;line-height:16px;margin-top:8px}
.contact-row svg{flex:none;margin-top:3px}
.footer-sep{position:absolute;top:992px;width:1px;height:140px;background:rgba(255,255,255,.18)}
.map{left:493px;top:1023px;width:159px;height:78px;background:linear-gradient(135deg,#e8e4d8,#f3e9b8 50%,#dce4cf)}
.bottombar{left:0;top:1155px;width:935px;height:45px;background:var(--brown)}
.copyright{left:106px;top:1171px;color:var(--white);font-size:10px}
.social{left:696px;top:1166px;display:flex;gap:4px}
.social i{width:22px;height:22px;background:var(--white);display:block}
</style>
</head>
<body>
<div class="abs topbar"></div>
<div class="abs topbar-phone">
  <svg width="14" height="14" viewBox="0 0 24 24"><path fill="#fff" d="M6.6 10.8a15 15 0 0 0 6.6 6.6l2.2-2.2a1 1 0 0 1 1-.25 11 11 0 0 0 3.6.6 1 1 0 0 1 1 1V20a1 1 0 0 1-1 1A17 17 0 0 1 3 4a1 1 0 0 1 1-1h3.5a1 1 0 0 1 1 1c0 1.25.2 2.450.6 3.6a1 1 0 0 1-.25 1z"/></svg>
  (555) 218-4093
</div>
<div class="abs header"></div>
<div class="abs logo"><span class="logo-mark"></span><span class="logo-name">BrightHaven</span></div>
<nav class="abs nav">
  <span class="active">Home</span><span>About Us</span><span>Services</span><span>Patient Resources</span><span>FAQ</span><span>Contact</span>
</nav>

<div class="abs hero"></div>
<div class="abs hero-photo" role="img" aria-label="Photo of a smiling mother holding her baby"></div>
<div class="abs form-panel"></div>
<div class="abs form-tab">Patient Forms</div>
<div class="field" style="left:130px;top:167px">Full name</div>
<div class="field" style="left:296px;top:167px">Email</div>
<div class="field" style="left:130px;top:205px">Phone number</div>
<div class="field" style="left:296px;top:205px">Appointment date</div>
<div class="field" style="left:130px;top:243px">Doctor</div>
<div class="field select" style="left:296px;top:243px">Select specialization</div>
<div class="abs form-submit">Make An Appointment Now</div>

<div class="abs steps"></div>
<div class="step" style="left:132px">
  <svg width="62" height="62" viewBox="0 0 62 62"><circle cx="31" cy="31" r="31" fill="#111"/><circle cx="31" cy="31" r="24" fill="#fff"/><circle cx="31" cy="31" r="19" fill="#111"/><rect x="20" y="25" width="16" height="10" fill="#fff"/><path d="M36 28h4l3 4v3h-7z" fill="#fff"/><circle cx="24" cy="37" r="2.5" fill="#fff"/><circle cx="39" cy="37" r="2.5" fill="#fff"/></svg>
  <div class="step-label">Select<br>A Service</div>
</div>
<div class="step" style="left:298px">
  <svg width="62" height="62" viewBox="0 0 62 62"><circle cx="31" cy="31" r="31" fill="#111"/><circle cx="31" cy="31" r="24" fill="#fff"/><circle cx="31" cy="31" r="19" fill="#111"/><rect x="22" y="22" width="18" height="18" rx="2" fill="#fff"/><rect x="22" y="22" width="18" height="5" fill="#888"/><text x="31" y="37" font-size="8" text-anchor="middle" font-family="Arial" fill="#111">12</text></svg>
  <div class="step-label">Choose Your<br>Schdule</div>
</div>
<div class="step" style="left:474px">
  <svg width="62" height="62" viewBox="0 0 62 62"><circle cx="31" cy="31" r="31" fill="#111"/><circle cx="31" cy="31" r="24" fill="#fff"/><circle cx="31" cy="31" r="19" fill="#111"/><path d="M24 20v8a6 6 0 0 0 12 0v-8M30 34v4a5 5 0 0 0 10 0v-4" stroke="#fff" stroke-width="2" fill="none"/><circle cx="40" cy="32" r="2.5" fill="#fff"/></svg>
  <div class="step-label">Cooose You<br>Doctor</div>
</div>
<div class="step" style="left:651px">
  <svg width="62" height="62" viewBox="0 0 62 62"><circle cx="31" cy="31" r="31" fill="#111"/><circle cx="31" cy="31" r="24" fill="#fff"/><circle cx="31" cy="31" r="19" fill="#111"/><path d="M28 20v13l-3-2-2 2 6 8h9l1-9-7-2v-10z" fill="#fff"/></svg>
  <div class="step-label">Request For<br>Appointment</div>
</div>
<svg class="dots" style="left:243px" width="60" height="18" viewBox="0 0 60 18"><path d="M0 9h48" stroke="#2f6800" stroke-width="3" stroke-dasharray="3 3"/><path d="M46 1l8 8-8 8" stroke="#2f6800" stroke-width="3" stroke-dasharray="3 3" fill="none"/></svg>
<svg class="dots" style="left:424px" width="60" height="18" viewBox="0 0 60 18"><path d="M0 9h48" stroke="#2f6800" stroke-width="3" stroke-dasharray="3 3"/><path d="M46 1l8 8-8 8" stroke="#2f6800" stroke-width="3" stroke-dasharray="3 3" fill="none"/></svg>
<svg class="dots" style="left:596px" width="60" height="18" viewBox="0 0 60 18"><path d="M0 9h48" stroke="#2f6800" stroke-width="3" stroke-dasharray="3 3"/><path d="M46 1l8 8-8 8" stroke="#2f6800" stroke-width="3" stroke-dasharray="3 3" fill="none"/></svg>

<h2 class="abs section-title" style="left:104px;top:537px">Welcome To Our Center</h2>
<div class="abs rule" style="left:104px;top:564px;width:720px"></div>
<div class="abs video" role="img" aria-label="Video still of a mother and child hugging"></div>
<svg class="abs" style="left:223px;top:659px" width="34" height="24" viewBox="0 0 34 24"><rect width="34" height="24" rx="6" fill="#222"/><path d="M13 7l9 5-9 5z" fill="#fff"/></svg>
<div class="abs video-bar"></div>
<svg class="abs" style="left:104px;top:726px" width="290" height="29" viewBox="0 0 290 29"><rect x="4" y="3" width="26" height="23" fill="#2c3943"/><path d="M12 8l10 6.5-10 6.5z" fill="#fff"/><path d="M38 11h3l4-3v13l-4-3h-3z" fill="#fff"/><path d="M48 10a5 5 0 0 1 0 9" stroke="#fff" fill="none"/><rect x="55" y="10" width="159" height="9" rx="4" fill="#0d1216" stroke="#555"/><rect x="57" y="12" width="74" height="5" rx="2.5" fill="#2d7fd1"/></svg>
<p class="abs body-text">Lorem ipsum dolor sit amet, consectetur adipiscing elit. Donec suscipit risus nec sagittis fermentum. Ut volutpat, metus vel auctor condimentum, augue neque blandit nunc, eget interdum neque dolor semper lacus. Praesent vel lacus nulla. Etiam vehicula ante Lorem ipsum dolor sit amet, consectetur adipiscing elit. Donec suscipit risus nec sagittis fermentum. Ut volutpat, metus vel auctor condimentum, augue neque blandit nunc, eget interdum neque dolor semper lacus. Praesent vel lacus nulla. Etiam vehicula ante&nbsp; Lorem ipsum dolor sit amet, consectetur adipiscing elit. Donec suscipit risus nec sagittis fermentum. Ut volutpat, metus vel auctor condimentum, augue neque blandit nunc, eget interdum neque dolor semper lacus.</p>

<div class="abs lower"></div>
<div class="abs divider-v"></div>
<h2 class="abs section-title" style="left:104px;top:799px">Why Choose Us</h2>
<div class="abs rule" style="left:104px;top:825px;width:300px"></div>
<p class="abs why-item" style="top:840px">Lorem ipsum dolor sit tetu adipiscing elised diam nonummy nibh euismod</p>
<p class="abs why-item" style="top:889px">Lorem ipsum dolor sit tetu adipiscing elised diam nonummy nibh euismod</p>
<div class="abs read-more"><span>Read More</span><b>»</b></div>

<h2 class="abs section-title" style="left:523px;top:799px">What Client say</h2>
<svg class="abs" style="left:802px;top:802px" width="22" height="14" viewBox="0 0 22 14"><path d="M7 1L2 7l5 6M15 1l5 6-5 6" stroke="#2f6800" stroke-width="2.5" fill="none"/></svg>
<div class="abs rule" style="left:523px;top:825px;width:300px"></div>
<div class="abs quote-box">
  <p class="quote-text">“ Lorem ipsum dolor sit amet, consectet adip iscing elit, sed diam nonummy nibh eui smod tincidunt ut laoreet dolore magna ali quam erat volutpat. ”</p>
  <div class="quote-name">Daniel Morrow, Ceo</div>
</div>
<div class="abs avatar" role="img" aria-label="Portrait photo of the client"></div>

<div class="abs footer"></div>
<div class="footer-col" style="left:105px;width:161px">
  <h3 style="font-weight:400">Quick Links</h3>
  <div class="footer-rule"></div>
  <ul class="quick-links"><li>Home</li><li>About Us</li><li>Services</li><li>Faq</li><li>Patient Resources</li><li>Contact Us</li></ul>
</div>
<div class="footer-sep" style="left:277px"></div>
<div class="footer-col" style="left:293px;width:161px">
  <h3>Contact Us</h3>
  <div class="footer-rule"></div>
  <div class="contact-row" style="margin-top:8px"><svg width="9" height="12" viewBox="0 0 9 12"><path d="M4.5 0A4.5 4.5 0 0 0 0 4.5C0 8 4.5 12 4.5 12S9 8 9 4.5A4.5 4.5 0 0 0 4.5 0z" fill="#fff"/><circle cx="4.5" cy="4.5" r="1.6" fill="#2f6800"/></svg><span style="width:125px">Lorem ipsum dolor sit Orchard Lane No 12, zip Code: 40213</span></div>
  <div class="contact-row" style="font-size:11px;margin-top:10px"><svg width="11" height="11" viewBox="0 0 24 24"><path fill="#fff" d="M6.6 10.8a15 15 0 0 0 6.6 6.6l2.2-2.2a1 1 0 0 1 1-.25 11 11 0 0 0 3.6.6 1 1 0 0 1 1 1V20a1 1 0 0 1-1 1A17 17 0 0 1 3 4a1 1 0 0 1 1-1h3.5a1 1 0 0 1 1 1c0 1.25.2 2.45.6 3.6a1 1 0 0 1-.25 1z"/></svg><span>(555) 730-1164</span></div>
  <div class="contact-row" style="font-size:11px"><svg width="12" height="9" viewBox="0 0 12 9"><rect width="12" height="9" fill="#fff"/><path d="M0 0l6 5 6-5" stroke="#2f6800" fill="none"/></svg><span>info@brighthaven.example</span></div>
</div>
<div class="footer-sep" style="left:468px"></div>
<div class="footer-col" style="left:490px;width:161px">
  <h3>Contact Map</h3>
  <div class="footer-rule"></div>
</div>
<div class="abs map" role="img" aria-label="Street map showing the clinic location"></div>
<div class="footer-sep" style="left:680px"></div>

<div class="abs bottombar"></div>
<div class="abs copyright">© 2014 Bright Haven. All Rights Reserved.</div>
<div class="abs social"><i></i><i></i><i></i><i></i><i></i></div>
</body>
</html>
```